Outdoor group fitness training - Greta Moxley Personal Training

I want an eye catching A4 flyer that promotes my two outdoor fitness groups. I have uploaded photos of each location: Mylor and Pasadena.
The target group is existing and potential new Personal training clients - all adults. There are two morning groups at Mylor ; one evening and one morning group at Pasadena. The groups will be for up to 8 people and are for all fitness levels.I want to encourage people to come and have a go. I have also uploaded a design I have used through printhollow for a previous flyer. I would like to use the orange graphic of the two people at the bottom of this design.
Cost is $15 per person
Location and times - Brackenridge Oval Wednesdays 7.30am; Sundays 8am
Corvale High School Thursdays 6.30pm: Saturdays 8am
Updates

Thanks so much to all of you for submitting a great set of designs. it was really hard making a choice in the end, and I really appreciate the promptness and creativity that went into the designs. I will certainly keep you in mind for future jobs. Cheers and have a great day Greta Moxley

Target Market(s)

40 - 60 year old adults: cross section of professionals, tradespeople and retirees. People who will enjoy socialising while also getting fit. No extremely fit people - cross section of beginners to intermediate; males and females

Industry/Entity Type

Training

Font styles to use
Sans Serif

Colors
f78f20
9bcb3c
ecf7fb

Requirements
Must have
• Fast turnaround required - within two days
Bright and attention grabbing, engaging. Could be A4 or could be postcard size?

State cost clearly
State that first 5 people to join either group will get first session at half price

```html
<!DOCTYPE html>
<html lang="en">
<head>
<meta charset="utf-8">
<title>Outdoor Group Fitness Training – Greta Moxley</title>
<link rel="stylesheet" href="https://fonts.googleapis.com/css2?family=Fira+Sans+Condensed:ital,wght@0,300;0,400;0,700;1,300;1,400&family=Fira+Sans+Extra+Condensed:wght@200;700;800&display=swap">
<style>
  :root {
    --stage: #5b5e64;
    --green-deep: #4f8a1f;
    --green-mid: #6eae2c;
    --green-bright: #8cc63f;
    --band-green: #8dc641;
    --ice: #ecf7fb;
    --orange: #f78f20;
    --ink: #2b2b2b;
    --band-dark: #2e2e2e;
    --shadow-green: rgba(40, 80, 10, 0.55);
  }
  * { box-sizing: border-box; margin: 0; padding: 0; }
  html, body {
    width: 1200px; height: 1000px; overflow: hidden;
    background: var(--stage);
  }
  .flyer {
    position: absolute; left: 274px; top: 38px;
    width: 648px; height: 917px;
    background: radial-gradient(ellipse 70% 55% at 55% 62%, var(--green-bright) 0%, var(--green-mid) 55%, var(--green-deep) 100%);
    box-shadow: 0 2px 10px rgba(0,0,0,0.45);
    overflow: hidden;
    font-family: "Fira Sans Condensed", sans-serif;
    color: var(--ice);
  }
  .headline {
    position: absolute; left: 0; top: 0; width: 648px; height: 430px;
    overflow: visible;
  }
  .headline text { fill: var(--ice); }
  .headline .shadow { fill: var(--shadow-green); }
  .headline-outdoor {
    font-family: "Fira Sans Extra Condensed", sans-serif;
    font-weight: 200; font-size: 113px;
  }
  .headline-group, .headline-training {
    font-family: "Fira Sans Extra Condensed", sans-serif;
    font-weight: 800; font-size: 174px;
  }
  .trainer {
    position: absolute; top: 426px; left: 0; right: 0; text-align: center;
    font-size: 30px; font-weight: 400; padding-left: 40px; white-space: nowrap;
  }
  .trainer em { font-style: italic; font-weight: 300; margin-right: 6px; }
  .trainer-dot {
    display: inline-block; width: 12px; height: 12px; border-radius: 50%;
    background: var(--ice); margin-left: 10px; vertical-align: 3px;
  }
  .cta {
    position: absolute; top: 486px; left: 0; right: 0; text-align: center;
    font-size: 27px; font-weight: 300;
  }
  .phone {
    position: absolute; top: 512px; left: 0; right: 0; text-align: center;
    font-family: "Fira Sans Extra Condensed", sans-serif;
    font-weight: 700; font-size: 66px; line-height: 1.1; white-space: nowrap;
    text-shadow: 3px 3px 0 var(--shadow-green);
  }
  .phone .paren { font-weight: 200; }
  .offer-band {
    position: absolute; top: 590px; left: 0; width: 100%; height: 30px;
    background: var(--band-dark); color: #fff; white-space: nowrap;
    font-size: 19px; font-weight: 300; text-align: center; line-height: 30px;
  }
  .offer-band strong { font-weight: 700; }
  .location-photo { position: absolute; top: 624px; height: 183px; }
  .location-photo.brackenridge {
    left: 0; width: 324px;
    background: linear-gradient(180deg, #dfe9ee 0%, #9fb07a 22%, #55702f 40%, #8a9178 62%, #8e8a82 100%);
  }
  .location-photo.corvale {
    left: 324px; width: 324px; border-left: 2px solid #fff;
    background: linear-gradient(180deg, #e7eff2 0%, #6e8a44 28%, #4d7325 48%, #6e8f38 70%, #777a76 100%);
  }
  .price-burst {
    position: absolute; left: 243px; top: 640px; width: 166px; height: 166px;
  }
  .price-burst svg { position: absolute; inset: 0; }
  .price-amount {
    position: absolute; left: 0; right: 0; top: 26px; text-align: center;
    font-family: "Fira Sans Extra Condensed", sans-serif; font-weight: 800;
    font-size: 88px; line-height: 1; color: #fff; letter-spacing: -2px;
  }
  .price-amount .currency { font-size: 62px; vertical-align: 14px; margin-right: 2px; }
  .price-unit {
    position: absolute; left: 0; right: 0; top: 114px; text-align: center;
    font-size: 12px; font-style: italic; font-weight: 300; color: #fff;
  }
  .schedule-band {
    position: absolute; top: 807px; left: 0; width: 100%; height: 110px;
    background: var(--band-green); border-top: 3px solid #fff;
    color: var(--ink);
  }
  .venue { position: absolute; top: 16px; white-space: nowrap; }
  .venue.left { left: 38px; }
  .venue.right { right: 36px; text-align: right; }
  .venue-name { font-weight: 700; font-size: 21px; line-height: 1.1; }
  .venue-times { font-style: italic; font-weight: 300; font-size: 17px; line-height: 1.1; }
  .venue.right .venue-times { text-transform: uppercase; font-size: 16px; }
  .brand-mark {
    position: absolute; left: 0; right: 0; top: 28px; text-align: center;
    font-weight: 700; font-size: 16px; color: var(--orange); white-space: nowrap;
  }
</style>
</head>
<body>
  <main class="flyer">
    <h1>
      <svg class="headline" viewBox="0 0 648 430" role="img" aria-label="Outdoor Group Fitness Training">
        <g aria-hidden="true">
          <text class="headline-outdoor shadow" x="57" y="140" textLength="534" lengthAdjust="spacingAndGlyphs">OUTDOOR</text>
          <text class="headline-group shadow" x="60" y="279" textLength="535" lengthAdjust="spacingAndGlyphs">GROUP FITNESS</text>
          <text class="headline-training shadow" x="65" y="416" textLength="530" lengthAdjust="spacingAndGlyphs">TRAINING</text>
        </g>
        <text class="headline-outdoor" x="54" y="137" textLength="534" lengthAdjust="spacingAndGlyphs">OUTDOOR</text>
        <text class="headline-group" x="56" y="275" textLength="535" lengthAdjust="spacingAndGlyphs">GROUP FITNESS</text>
        <text class="headline-training" x="61" y="412" textLength="530" lengthAdjust="spacingAndGlyphs">TRAINING</text>
      </svg>
    </h1>
    <p class="trainer"><em>with</em>GRETA MOXLEY<span class="trainer-dot"></span></p>
    <p class="cta">Call Now to Schedule</p>
    <p class="phone"><span class="paren">(</span>555<span class="paren">)</span> 123-9031</p>

    <p class="offer-band"><strong>First 5 people</strong> to join either group will get first session at <strong>HALF PRICE</strong></p>

    <div class="location-photo brackenridge" role="img" aria-label="Photo of Brackenridge Oval: gravel car park, shelter and gum trees"></div>
    <div class="location-photo corvale" role="img" aria-label="Photo of Corvale High School grounds: lawn, trees and footpath"></div>

    <div class="price-burst">
      <svg viewBox="0 0 100 100" aria-hidden="true">
        <polygon fill="var(--orange)" stroke="#fff" stroke-width="2.5" stroke-linejoin="round"
          points="100,50 92.2,58.4 96.2,69.2 85.7,73.9 85.4,85.4 73.9,85.7 69.2,96.2 58.4,92.2 50,100 41.6,92.2 30.8,96.2 26.1,85.7 14.6,85.4 14.3,73.9 3.8,69.2 7.8,58.4 0,50 7.8,41.6 3.8,30.8 14.3,26.1 14.6,14.6 26.1,14.3 30.8,3.8 41.6,7.8 50,0 58.4,7.8 69.2,3.8 73.9,14.3 85.4,14.6 85.7,26.1 96.2,30.8 92.2,41.6"/>
      </svg>
      <p class="price-amount"><span class="currency">$</span>15</p>
      <p class="price-unit">PER PERSON</p>
    </div>

    <footer class="schedule-band">
      <div class="venue left">
        <p class="venue-name">Brackenridge Oval</p>
        <p class="venue-times">Wednesdays 7.30am; Sundays 8am</p>
      </div>
      <p class="brand-mark">Greta Moxley</p>
      <div class="venue right">
        <p class="venue-name">Corvale High School</p>
        <p class="venue-times">Thursdays 6.30pm: Saturdays 8am</p>
      </div>
    </footer>
  </main>
</body>
</html>
```